Wordpress Design for a Private Label BBQ Brand

For our new brand, we'd need a new Wordpress website. We'd prefer to run the website on Wordpress

We'd like to include the following
- space for description of the brand
- space for product portfolio (not a shop!)
- space for socials
- space for support
- space for contact

```html
<!DOCTYPE html>
<html lang="en">
<head>
<meta charset="utf-8">
<title>Emberline – BBQ</title>
<link href="https://fonts.googleapis.com/css2?family=Libre+Caslon+Text:wght@400;700&family=Roboto:wght@400;500;700&display=swap" rel="stylesheet">
<style>
:root{
  --red:#c8151d;--red-dark:#a80f1a;--orange:#e2521c;--grad:linear-gradient(90deg,#e4471c,#c1121c);
  --pink:#f9ece9;--grey:#f2f2f3;--ink:#222;--muted:#555;--black:#050505;--white:#fff;
}
*{box-sizing:border-box;margin:0;padding:0}
html,body{width:1200px;height:4955px;overflow:hidden}
body{font-family:"Roboto",sans-serif;color:var(--ink);position:relative;background:#fff}
section,header,nav,footer{position:absolute;left:0;width:1200px}
.title{font-family:"Libre Caslon Text",serif;font-weight:700;font-size:28px;text-align:center;letter-spacing:.5px;text-transform:uppercase}
.btn{display:inline-flex;align-items:center;gap:10px;background:var(--grad);color:#fff;font-size:13px;font-weight:700;border-radius:22px;padding:0 22px;height:40px;text-transform:uppercase;white-space:nowrap}
.btn i{width:12px;height:12px;border-radius:50%;background:#fff;display:inline-block}
/* header */
.topbar{top:0;height:80px}
.brand{position:absolute;left:112px;top:20px;font-family:"Libre Caslon Text",serif;font-weight:700;font-size:34px;color:var(--ink)}
.search{position:absolute;left:601px;top:12px;width:358px;height:52px;border:1px solid #ddd;border-radius:26px;font-size:14px;color:#888;padding:17px 28px}
.search b{position:absolute;right:8px;top:9px;width:34px;height:34px;border-radius:50%;background:var(--grad)}
.account{position:absolute;left:996px;top:20px;font-size:13px;font-weight:700;text-align:center}
.account i{display:block;margin:0 auto 6px;width:10px;height:12px;background:#222;border-radius:5px 5px 2px 2px}
.menu{top:80px;height:50px;background:var(--grad);display:flex;align-items:center;padding-left:124px}
.menu a{color:#fff;font-size:15px;font-weight:700;text-transform:uppercase;text-decoration:none;white-space:nowrap}
.menu span{color:#fff;margin:0 38px;font-size:14px}
/* hero */
.hero{top:130px;height:640px;background:linear-gradient(100deg,#6f8a3a 0%,#a8863f 35%,#5f4a2d 60%,#39321f 100%)}
.hero-text{position:absolute;left:700px;top:190px;width:460px;color:#fff}
.hero-text h3{font-family:"Libre Caslon Text",serif;font-size:30px;font-weight:400;white-space:nowrap}
.hero-text h1{font-family:"Libre Caslon Text",serif;font-size:58px;font-weight:700;line-height:1.2;margin:10px 0 16px;white-space:nowrap}
.hero-text p{width:380px;font-size:15px;line-height:1.7;margin-bottom:26px}
/* about */
.about{top:770px;height:540px;background:var(--pink)}
.about-art{position:absolute;left:114px;top:40px;width:346px;height:456px;border-radius:50% 50% 48% 48% / 60% 60% 40% 40%;background:linear-gradient(160deg,#e35a2c,#b3281e 60%,#8d1c17)}
.about-copy{position:absolute;left:561px;top:80px;width:493px}
.about-copy h2{font-family:"Libre Caslon Text",serif;font-size:28px;font-weight:700;margin-bottom:22px}
.about-copy p{font-size:14.5px;line-height:1.77;text-align:justify;color:#333;margin-bottom:22px}
/* portfolio */
.portfolio{top:1310px;height:646px}
.portfolio .title{margin-top:80px}
.grid{position:absolute;left:112px;top:155px;display:grid;grid-template-columns:repeat(4,236px);grid-auto-rows:196px;gap:10px 11px}
.grid div{background:var(--grey);display:flex;align-items:center;justify-content:center}
.grid div span{width:60%;height:40%;background:linear-gradient(180deg,#6b6e73,#2a2b2e);border-radius:8px;opacity:.85}
/* social */
.social{top:1956px;height:613px;background:linear-gradient(180deg,#e4531b,#b3101c)}
.social .title{color:#fff;margin-top:80px}
.cards{position:absolute;left:112px;top:152px;display:flex;gap:30px}
.card{width:305px;height:384px;background:#fff;padding:18px 14px}
.card .head{display:flex;gap:10px;align-items:center;font-size:14px;font-weight:700}
.card .head i{width:36px;height:36px;border-radius:50%;background:#c9ccd2;flex:none}
.card .head small{display:block;font-size:11px;font-weight:500;margin-top:4px}
.card .pic{margin-top:12px;height:148px;background:linear-gradient(180deg,#3a2a20,#c4561e 60%,#4b2e1d)}
.card .stats{display:flex;gap:34px;font-size:14px;color:#444;margin-top:22px}
.card .acts{display:flex;gap:26px;font-size:13px;color:#1f54b8;margin-top:14px}
.card p{font-size:14px;line-height:1.7;color:#333;margin-top:12px}
.arrow{position:absolute;top:334px;width:14px;height:14px;border-top:2px solid #fff;border-left:2px solid #fff}
/* faq */
.faq{top:2569px;height:694px;background:linear-gradient(90deg,#f4efe9,#fbf6f2 50%,#f6d9c3)}
.faq .title{margin-top:82px;font-size:26px}
.faq-list{position:absolute;left:202px;top:168px;width:796px}
.q{height:52px;background:#fff;border-radius:26px;box-shadow:0 2px 8px rgba(0,0,0,.12);margin-bottom:23px;display:flex;align-items:center;justify-content:space-between;padding:0 24px;font-size:15.5px;font-weight:500;color:#222}
.q i{width:20px;height:20px;border-radius:50%;background:var(--red);flex:none}
.q.open{height:133px;flex-direction:column;align-items:stretch;justify-content:flex-start;padding:18px 26px;background:var(--grad);color:#fff}
.q.open .row{display:flex;justify-content:space-between}
.q.open i{background:#fff}
.q.open p{font-size:14px;font-weight:400;line-height:1.75;margin-top:14px}
/* forum */
.forum{top:3263px;height:587px;background:var(--red-dark)}
.forum .title{color:#fff;margin-top:90px}
.posts{position:absolute;left:115px;top:167px;display:flex;gap:19px}
.post{width:311px;height:330px;position:relative}
.post .img{height:192px;background:linear-gradient(180deg,#2c2b27,#b9541e 70%,#3a2319)}
.post .date{position:absolute;right:12px;top:18px;width:38px;height:48px;border-radius:6px;background:var(--orange);color:#fff;font-size:13px;font-weight:700;text-align:center;padding-top:6px;line-height:1.3}
.post .box{position:absolute;left:20px;right:0;top:192px;bottom:0;background:#fff;padding:20px 22px}
.post small{font-size:12px;color:#777}
.post h4{font-size:16px;line-height:1.5;margin:8px 0 12px}
.post .meta{font-size:12px;color:#666;display:flex;gap:20px}
/* contact */
.contact{top:3850px;height:1050px;background:linear-gradient(180deg,#f5ede6 0%,#efe2d6 41.7%,var(--black) 41.7%)}
.contact .title{margin-top:90px}
.quote{position:absolute;left:202px;top:198px;width:796px;height:486px;background:#fff;box-shadow:10px 10px 0 var(--red);padding:50px 58px}
.quote h3{text-align:center;font-size:30px;font-weight:700;margin-bottom:34px}
.fields{display:grid;grid-template-columns:1fr 1fr;gap:13px 13px}
.field{height:49px;border:1px solid #ccc;font-size:14px;color:#777;padding:15px 20px;position:relative}
.field i{position:absolute;right:18px;top:18px;width:12px;height:12px;background:#555;border-radius:2px}
.field.msg{grid-column:1/3;height:108px}
.submit{margin-top:30px;height:46px;border-radius:23px;background:var(--grad);color:#fff;text-align:center;font-size:14px;font-weight:700;line-height:46px}
.foot-brand{position:absolute;left:110px;top:935px;font-family:"Libre Caslon Text",serif;font-weight:700;font-size:40px;color:#fff;white-space:nowrap}
.fcol{position:absolute;top:755px;color:#fff;font-size:13px}
.fcol h5{font-size:14px;font-weight:700;margin-bottom:26px}
.fcol li{list-style:none;margin-bottom:16px;padding-left:26px;position:relative}
.fcol li:before{content:"»";position:absolute;left:0;color:var(--orange)}
.ci{display:flex;gap:16px;align-items:flex-start;margin-bottom:22px;line-height:1.5}
.ci i{width:24px;height:24px;border-radius:50%;background:#333;flex:none}
.sub p{width:250px;line-height:1.6;margin-bottom:20px}
.sub .mail{width:256px;height:46px;border-radius:23px;background:#fff;color:#555;padding:15px 50px;position:relative}
.sub .mail b{position:absolute;right:0;top:0;width:46px;height:46px;border-radius:50%;background:var(--grad)}
.dots{display:flex;gap:10px;margin-top:18px}
.dots i{width:30px;height:30px;border-radius:50%;background:var(--orange)}
.bottom{top:4900px;height:55px;background:var(--grad);color:#fff;font-size:14px;text-align:center;line-height:55px}
</style>
</head>
<body>
<header class="topbar">
  <div class="brand">EMBERLINE</div>
  <div class="search">Search Products<b></b></div>
  <div class="account"><i></i>My Accounts</div>
</header>
<nav class="menu">
  <a>Home</a><span>|</span><a>About Us</a><span>|</span><a>Products</a><span>|</span><a>Social Feed</a><span>|</span><a>FAQ</a><span>|</span><a>Forum</a><span>|</span><a>Contact Us</a>
</nav>
<section class="hero" role="img" aria-label="Photo of a smiling man grilling sausages at an outdoor family barbecue">
  <div class="hero-text">
    <h3>WELCOME TO</h3>
    <h1>EMBERLINE</h1>
    <p>Lorem ipsum dolor sited amet consectetur adipiscing elit, sed do eiusmod tempor incididunt uted labored.</p>
    <span class="btn">Get Started <i></i></span>
  </div>
</section>
<section class="about">
  <div class="about-art" role="img" aria-label="Flame-shaped photo of food on a hot grill"></div>
  <div class="about-copy">
    <h2>ABOUT US</h2>
    <p>Lorem ipsum dolor sit amet, consectetur adipiscing elit, sed do eiusmod tempor incididunt ut labore et dolore magna aliqua. Ut enim ad minim veniam, quis nostrud exercitation ullamco laboris nisi ut aliquip ex ea commodo consequat. Duis aute irure dolor in reprehenderit in voluptate velit esse cillum dolore eu fugiat nulla pariatur. Excepteur sint occaecat cupidatat non proident, sunt in culpa qui officia deserunt mollit anim id est laborumLorem ipsum dolor sit amet, consectetur adipiscing elit, sed do eiusmod tempor incididunt ut labore et dolore magna aliqua. Ut enim ad minim veniam, quis nostrud exercitation ullamco laboris nisi ut aliquip commodo consequat.</p>
    <span class="btn">Learn More <i></i></span>
  </div>
</section>
<section class="portfolio">
  <h2 class="title">Product Portfolio</h2>
  <div class="grid">
    <div role="img" aria-label="Pair of grill handles"><span></span></div>
    <div role="img" aria-label="Portable charcoal grill"><span></span></div>
    <div role="img" aria-label="Kamado grill on stand"><span></span></div>
    <div role="img" aria-label="Grill fork"><span></span></div>
    <div role="img" aria-label="Grill tongs"><span></span></div>
    <div role="img" aria-label="Meat claw fork"><span></span></div>
    <div role="img" aria-label="Round grill grate"><span></span></div>
    <div role="img" aria-label="Tool carry case"><span></span></div>
  </div>
</section>
<section class="social">
  <h2 class="title">Social Feed</h2>
  <div class="arrow" style="left:58px;transform:rotate(-45deg)"></div>
  <div class="arrow" style="left:1128px;transform:rotate(135deg)"></div>
  <div class="cards">
    <div class="card"><div class="head"><i></i><div>Lorem set consectetur<small>5:52 pm-Jun 24,2020</small></div></div><div class="pic" role="img" aria-label="Meat grilling over open flames"></div><div class="stats"><span>23</span><span>83</span><span>73</span></div><div class="acts"><span>Favorite</span><span>Share</span></div><p>Lorem ipsum dolor sit consectetur adipiscing elit, sed do set eiusmod</p></div>
    <div class="card"><div class="head"><i></i><div>Lorem set consectetur<small>5:52 pm-Jun 24,2020</small></div></div><div class="pic" role="img" aria-label="Man with a kettle grill outdoors" style="background:linear-gradient(180deg,#8fa85a,#d8b24a 60%,#4d5a2c)"></div><div class="stats"><span>23</span><span>83</span><span>73</span></div><div class="acts"><span>Favorite</span><span>Share</span></div><p>Lorem ipsum dolor sit consectetur adipiscing elit, sed do set eiusmod</p></div>
    <div class="card"><div class="head"><i></i><div>Lorem set consectetur<small>5:52 pm-Jun 24,2020</small></div></div><div class="pic" role="img" aria-label="Steaks on a flaming grill"></div><div class="stats"><span>23</span><span>83</span><span>73</span></div><div class="acts"><span>Favorite</span><span>Share</span></div><p>Lorem ipsum dolor sit consectetur adipiscing elit, sed do set eiusmod</p></div>
  </div>
</section>
<section class="faq">
  <h2 class="title">FAQ</h2>
  <div class="faq-list">
    <div class="q">Lorem ipsum dolor sit amet, consectetur adipiscing elit, sed do eiusmod<i></i></div>
    <div class="q">Lorem ipsum dolor sit amet, consectetur adipiscing<i></i></div>
    <div class="q">Sed ut perspiciatis unde omnis iste natus error sit voluptatem accusantium doloremque<i></i></div>
    <div class="q">Nemo enim ipsam voluptatem quia voluptas sit aspernatur aut odit aut fugit, sed<i></i></div>
    <div class="q open"><div class="row">Sed ut perspiciatis unde omnis iste natus error sit voluptatem<i></i></div><p>Duis aute irure dolor in reprehenderit in voluptate velit esse cillum dolore eu fugiat nulla pariatur. Excepteur occaecat cupidatat non proident, sunt in culpa qui officia deserunt mollit anim id est laborum.</p></div>
  </div>
</section>
<section class="forum">
  <h2 class="title">Forum</h2>
  <div class="posts">
    <div class="post"><div class="img" role="img" aria-label="Charcoal grill with flames at night"></div><div class="date">Jan<br>10</div><div class="box"><small>Lorem ipsum dolor</small><h4>Lorem ipsum dolor sit amet sed consectetur dolor sictea.</h4><div class="meta"><span>John Doe</span><span>0 Comments</span></div></div></div>
    <div class="post"><div class="img" role="img" aria-label="Woman grilling by a lake" style="background:linear-gradient(180deg,#7c9a8c,#3f5f58 60%,#2a3a33)"></div><div class="date">Jan<br>10</div><div class="box"><small>Lorem ipsum dolor</small><h4>Lorem ipsum dolor sit amet sed consectetur dolor sictea.</h4><div class="meta"><span>John Doe</span><span>0 Comments</span></div></div></div>
    <div class="post"><div class="img" role="img" aria-label="Skewers on a hot grill"></div><div class="date">Jan<br>10</div><div class="box"><small>Lorem ipsum dolor</small><h4>Lorem ipsum dolor sit amet sed consectetur dolor sictea.</h4><div class="meta"><span>John Doe</span><span>0 Comments</span></div></div></div>
  </div>
</section>
<section class="contact">
  <h2 class="title">Contact Us</h2>
  <div class="quote">
    <h3>Request A Quote</h3>
    <div class="fields">
      <div class="field">First Name<i></i></div><div class="field">Last Name<i></i></div>
      <div class="field">Email Address<i></i></div><div class="field">Phone no<i></i></div>
      <div class="field msg">Message<i></i></div>
    </div>
    <div class="submit">SUBMIT NOW</div>
  </div>
  <div class="foot-brand">EMBERLINE</div>
  <div class="fcol" style="left:420px"><h5>QUICK LINKS</h5><ul><li>Home</li><li>About Us</li><li>Products</li><li>Social Feed</li><li>FAQ</li><li>Forum</li><li>Contact Us</li></ul></div>
  <div class="fcol" style="left:595px"><h5>CONTACT US</h5><div class="ci"><i></i><b>+ 888 888 8888</b></div><div class="ci"><i></i>info@emberline.com</div><div class="ci"><i></i>114 Lorem ipsum dolor sit<br>adipiscing sed do eiusmod</div></div>
  <div class="fcol sub" style="left:835px"><h5>SUBSCRIBE NOW</h5><p>Sign up to our newsletter and stay up to date</p><div class="mail">Email Address<b></b></div><div class="dots"><i></i><i></i><i></i><i></i></div></div>
</section>
<footer class="bottom">© 2023 Emberline. All Rights Reserved</footer>
</body>
</html>
```